RW Hollis LLC Business Card - Civil Engineering & Consulting Firm

We need a Business Card that is elegant, and masculine.  It is our Professional Civil Engineering & Consulting Company located in San Antonio TX (Not s construction or builder firm- no gears & no tool images please). We provide civil engineering services including  commercial site plans, grading and drainage plans, utility plans, hydraulics and hydrology, land planning, utility coordination, and other general civil engineering services related to commercial and residential development.
We have 2 existing Logos. We would like to convey reliability, strength, trustworthiness and attention to detail.  Blues and orange tones as per logo We are OK with the use of a darker blue in the mix.  We have 2 logo versions - Full Company Name Logo to go on the back of card, & Small Icon Logo for the front w/ personal Info.

Target Market(s)
Architects, Real Estate Developers, Other Strctural Engineers, Surveyers, General Contractors
Industry/Entity Type
Professional Civil Engineering
Contact Information for Business Card
Name, Position, Address, Cell & Office #, email, and company website
Font styles to use
Other font styles liked:
- Avian
Requirements
Should not have
- No Tools, No Gears, no Cranes, or Construction Equipment.

```html
<!DOCTYPE html>
<html lang="en">
<head>
<meta charset="utf-8">
<title>RW Hollis LLC – Business Card</title>
<link rel="stylesheet" href="https://fonts.googleapis.com/css2?family=Carlito:ital,wght@0,400;0,700;1,400&display=swap">
<style>
  :root {
    --backdrop: #a7a8ab;
    --paper: #ffffff;
    --ink: #2b2b2b;
    --navy-top: #130a42;
    --navy-bottom: #020032;
    --band-navy: #0a0036;
    --stripe-gold: #fbb714;
    --sky-blue: #7aaedb;
    --orange: #f39530;
  }
  * { margin: 0; padding: 0; box-sizing: border-box; }
  html, body {
    width: 1200px;
    height: 960px;
    overflow: hidden;
    background: var(--backdrop);
    font-family: "Carlito", "Calibri", sans-serif;
    color: var(--ink);
  }
  .card {
    position: absolute;
    width: 772px;
    height: 442px;
    overflow: hidden;
  }

  /* Front */
  .card-front {
    left: 161px;
    top: 35px;
    background: var(--paper);
  }
  .front-stripe {
    position: absolute;
    left: 0; right: 0;
    top: 406px;
    height: 7px;
    background: var(--stripe-gold);
  }
  .front-band {
    position: absolute;
    left: 0; right: 0;
    top: 413px;
    bottom: 0;
    background: var(--band-navy);
  }
  .front-brand {
    position: absolute;
    left: 92px;
    top: 150px;
    width: 180px;
    display: flex;
    flex-direction: column;
    gap: 14px;
  }
  .brand-square {
    width: 26px;
    height: 26px;
    background: var(--sky-blue);
  }
  .front-brand-name {
    font-size: 34px;
    line-height: 1.05;
    font-weight: 700;
    color: var(--orange);
  }
  .person {
    position: absolute;
    left: 466px;
    top: 88px;
  }
  .person-name {
    font-size: 36px;
    font-style: italic;
    font-weight: 400;
    line-height: 1;
    letter-spacing: 0.5px;
  }
  .person-role {
    font-size: 19px;
    margin-top: 6px;
  }
  .address {
    position: absolute;
    left: 466px;
    top: 180px;
    font-size: 19px;
    line-height: 22px;
    font-style: normal;
  }
  .contact-list {
    position: absolute;
    left: 466px;
    list-style: none;
    font-size: 19px;
  }
  .contact-list.phones { top: 247px; }
  .contact-list.online { top: 318px; }
  .contact-list li {
    display: flex;
    align-items: center;
    height: 27px;
  }
  .contact-icon {
    width: 18px;
    height: 18px;
    margin-right: 17px;
    fill: var(--ink);
  }

  /* Back */
  .card-back {
    left: 266px;
    top: 504px;
    background: linear-gradient(180deg, var(--navy-top) 0%, var(--navy-bottom) 100%);
  }
  .back-brand {
    position: absolute;
    left: 0; right: 0;
    top: 188px;
    display: flex;
    justify-content: center;
    align-items: center;
    gap: 18px;
  }
  .back-brand .brand-square {
    width: 34px;
    height: 34px;
    background: var(--orange);
  }
  .back-brand-name {
    font-size: 58px;
    font-weight: 400;
    letter-spacing: 6px;
    color: var(--sky-blue);
    line-height: 1;
  }
</style>
</head>
<body>

<section class="card card-front" aria-label="Business card front">
  <div class="front-brand">
    <span class="brand-square"></span>
    <span class="front-brand-name">RW Hollis LLC</span>
  </div>

  <div class="person">
    <h1 class="person-name">Name Title</h1>
    <p class="person-role">designation</p>
  </div>

  <address class="address">
    suit # 00, Lorem ipsum<br>
    Lorem Lorem ipsum
  </address>

  <ul class="contact-list phones">
    <li>
      <svg class="contact-icon" viewBox="0 0 18 18" aria-hidden="true">
        <rect x="0" y="0" width="18" height="18" rx="3"/>
        <path d="M6 3.5 L8 3.5 L8.5 6.5 L7 7.5 Q8 10.5 10.5 11.5 L11.5 10 L14.5 10.5 L14.5 12.5 Q14 14.5 11.5 14.3 Q5 13 3.7 6.5 Q3.6 3.8 6 3.5 Z" fill="#fff"/>
      </svg>
      000-000-0000
    </li>
    <li>
      <svg class="contact-icon" viewBox="0 0 18 18" aria-hidden="true">
        <rect x="5" y="0" width="8" height="7"/>
        <rect x="0" y="8" width="18" height="7" rx="1.5"/>
        <rect x="3" y="15" width="12" height="3"/>
        <rect x="4" y="10" width="10" height="1.5" fill="#fff"/>
      </svg>
      000-000-0000
    </li>
  </ul>

  <ul class="contact-list online">
    <li>
      <svg class="contact-icon" viewBox="0 0 18 18" aria-hidden="true">
        <path d="M0 7 L9 1 L18 7 L18 17 L0 17 Z"/>
        <path d="M2 8 L9 13 L16 8" stroke="#fff" stroke-width="1.5" fill="none"/>
      </svg>
      abcd@KestrelGroupAB.com
    </li>
    <li>
      <svg class="contact-icon" viewBox="0 0 18 18" aria-hidden="true">
        <path d="M6 1.5 Q6 0 7.3 0 Q8.5 0 8.5 1.5 L8.5 7 L14 8 Q16 8.5 15.5 11 L14.5 16 Q14 18 12 18 L8 18 Q6.5 18 5.5 16.5 L2.5 12 Q1.8 10.5 3.2 10 Q4.2 9.7 5 11 L6 12 Z"/>
      </svg>
      www.KestrelGroupAB.com
    </li>
  </ul>

  <div class="front-stripe"></div>
  <div class="front-band"></div>
</section>

<section class="card card-back" aria-label="Business card back">
  <div class="back-brand">
    <span class="brand-square"></span>
    <span class="back-brand-name">RW Hollis LLC</span>
  </div>
</section>

</body>
</html>
```